Comprehensive guide for the front desk medical office staff.

selling a reference guide for the front desk personnel at Urgent Care clinics

Target Market(s)

Urgent Care and physian office manager s

Industry/Entity Type

Medical

```html
<!DOCTYPE html>
<html lang="en">
<head>
<meta charset="utf-8">
<title>Front Desk Reference Guide – Postcard</title>
<link rel="stylesheet" href="https://fonts.googleapis.com/css2?family=Oswald:wght@600;700&family=Lato:ital,wght@0,400;0,700;1,400;1,700&display=swap">
<style>
  :root {
    --leaf: #5f7b0e;
    --leaf-dark: #3c5712;
    --cream: #f4eee2;
    --ink: #1d1d1d;
    --paper: #ffffff;
    --page: #ffffff;
    --rule: #c9c9c9;
  }
  * { box-sizing: border-box; margin: 0; padding: 0; }
  html, body { width: 889px; height: 1200px; overflow: hidden; background: var(--page); }
  body { position: relative; font-family: "Lato", sans-serif; color: var(--ink); }

  .card { position: absolute; left: 42px; width: 805px; background: var(--paper); overflow: hidden; }
  .card--front { top: 30px; height: 545px; }
  .card--back { top: 610px; height: 541px; }
  .card__shapes { position: absolute; inset: 0; width: 100%; height: 100%; }

  .headline { font-family: "Oswald", sans-serif; font-weight: 700; line-height: 1.06; letter-spacing: 0.2px; }
  .subline { font-style: italic; font-weight: 700; line-height: 1.3; }

  /* Front */
  .front__tagline { position: absolute; left: 33px; top: 38px; width: 260px; font-style: italic; font-size: 14px; color: var(--leaf); }
  .front__titlebox { position: absolute; left: 30px; top: 62px; width: 248px; height: 121px; border: 1px dashed var(--rule); text-align: center; padding-top: 8px; }
  .front__titlebox .headline { font-size: 27px; color: var(--ink); }
  .front__titlebox .subline { font-size: 17px; color: var(--ink); margin-top: 2px; }
  .front__blurb { position: absolute; left: 34px; top: 230px; width: 250px; font-size: 14.5px; line-height: 20px; color: var(--paper); }
  .front__blurb .line { display: block; text-align: justify; text-align-last: justify; white-space: nowrap; }
  .front__blurb .line--last { text-align-last: left; }
  .order { text-align: center; color: var(--paper); }
  .order__lead { font-style: italic; font-weight: 700; }
  .order__phone { font-family: "Oswald", sans-serif; font-weight: 700; line-height: 1.1; }
  .order__price sup { font-size: 0.6em; }
  .order__ship { font-style: italic; }
  .front__order { position: absolute; left: 34px; top: 405px; width: 250px; }
  .front__order .order__lead { font-size: 15px; }
  .front__order .order__phone { font-size: 30px; }
  .front__order .order__price { font-size: 19px; }
  .front__order .order__ship { font-size: 12px; margin-top: 2px; }
  .front__impression { position: absolute; left: 400px; top: 389px; width: 380px; text-align: center; font-style: italic; font-weight: 700; font-size: 22px; color: var(--ink); }
  .front__slogan { position: absolute; left: 380px; top: 438px; width: 400px; text-align: center; font-size: 28px; color: var(--paper); line-height: 1.28; }

  /* Back */
  .back__title { position: absolute; left: 42px; top: 34px; width: 250px; border-top: 1px solid #d9e2bf; border-bottom: 1px solid #d9e2bf; padding: 12px 0 10px; text-align: center; color: var(--paper); }
  .back__title .headline { font-size: 28px; }
  .back__title .subline { font-size: 18px; margin-top: 3px; }
  .back__intro { position: absolute; left: 46px; top: 172px; width: 270px; font-style: italic; font-size: 18.5px; line-height: 23.5px; color: var(--paper); white-space: nowrap; }
  .features { position: absolute; left: 50px; top: 283px; width: 260px; list-style: none; color: var(--paper); font-size: 13.5px; line-height: 21.6px; white-space: nowrap; }
  .features li { position: relative; padding-left: 22px; }
  .features li::before { content: "✓"; position: absolute; left: 0; top: 0; font-weight: 700; font-size: 15px; }
  .back__more { position: absolute; left: 75px; top: 458px; width: 200px; text-align: center; font-style: italic; font-weight: 700; font-size: 13.5px; color: var(--paper); }
  .back__order { position: absolute; left: 307px; top: 10px; width: 186px; height: 186px; border-radius: 50%; background: var(--leaf-dark); padding-top: 34px; }
  .back__order .order__lead { font-size: 19px; font-weight: 400; }
  .back__order .order__phone { font-size: 29px; }
  .back__order .order__price { font-size: 19px; }
  .back__order .order__ship { font-size: 14px; font-style: normal; line-height: 1.3; }
</style>
</head>
<body>

<section class="card card--front">
  <svg class="card__shapes" viewBox="0 0 805 545">
    <defs>
      <linearGradient id="photoTone" x1="0" y1="0" x2="1" y2="1">
        <stop offset="0" stop-color="#e9ecdc"/>
        <stop offset="0.45" stop-color="#b9d24a"/>
        <stop offset="1" stop-color="#d8d2c4"/>
      </linearGradient>
    </defs>
    <polygon points="387,0 805,0 805,425 387,425 285,195" fill="url(#photoTone)" role="img" aria-label="Photo of a smiling doctor and receptionist at a bright green front desk"/>
    <path d="M377,356 Q560,338 805,350 L805,425 L387,425 Z" fill="var(--cream)"/>
    <polygon points="0,189 285,202 387,425 805,425 805,545 0,545" fill="var(--leaf)"/>
  </svg>

  <p class="front__tagline">Make each patient visit a success with</p>
  <div class="front__titlebox">
    <h1 class="headline">The FRONT DESK<br>REFERENCE GUIDE</h1>
    <p class="subline">for Urgent Care Centers &amp;<br>Physician Offices</p>
  </div>
  <p class="front__blurb">
    <span class="line">A complete up-to-date resource</span>
    <span class="line">perfect for training, reference,</span>
    <span class="line">and best practices. Created by a</span>
    <span class="line">healthcare administrator with over</span>
    <span class="line">a decade of experience. A “cheat</span>
    <span class="line">sheet” of all the information your</span>
    <span class="line line--last">front desk needs in one place!</span>
  </p>
  <div class="order front__order">
    <p class="order__lead">To order call</p>
    <p class="order__phone">555-014-2290</p>
    <p class="order__price">Only $99.<sup>99</sup></p>
    <p class="order__ship">plus $7.00 shipping and handling</p>
  </div>
  <p class="front__impression">Make a great first impression!</p>
  <p class="front__slogan headline">PATIENT EXPERIENCE<br>BEGINS at the FRONT DESK</p>
</section>

<section class="card card--back">
  <svg class="card__shapes" viewBox="0 0 805 541" aria-hidden="true">
    <polygon points="0,0 375,0 302,541 0,541" fill="var(--leaf)"/>
  </svg>

  <div class="back__title">
    <h2 class="headline">The FRONT DESK<br>REFERENCE GUIDE</h2>
    <p class="subline">for Urgent Care Centers &amp;<br>Physician Offices</p>
  </div>
  <p class="back__intro">All the information your front<br>desk needs -&nbsp; in one place!<br>Perfect for raining, reference,<br>best practices, and more.</p>
  <ul class="features">
    <li>Front desk process flow.</li>
    <li>Glossary of medical terminology.</li>
    <li>HIPPA guidelines for office staff.</li>
    <li>Introduction to insurance carriers,<br>coverage,&nbsp; and plan types.</li>
    <li>The anatomy of an insurance card.</li>
    <li>Understanding worker’s<br>compensation &amp; required&nbsp; forms.</li>
  </ul>
  <p class="back__more">and much more!</p>

  <div class="order back__order">
    <p class="order__lead">To order call</p>
    <p class="order__phone">555-014-2290</p>
    <p class="order__price">Only $99.<sup>99</sup></p>
    <p class="order__ship">plus $7.00 shipping<br>and handling</p>
  </div>
</section>

</body>
</html>
```